Crestline Gas and Plumbing Business Card Design

I am after a business card design for my plumbing business called 'Crestline Gas & Plumbing'. I do all types of plumbing and gas work and specialise in general maintenance plumbing. Would like to see designs using current logo

Industry/Entity Type

Plumbing

Contact Information for Business Card

Name - Dale Whitcombe
Phone number - 0455163027
Email - admin@crestlinegasandplumbing.example.com.au
ABN - 68204915336

```html
<!DOCTYPE html>
<html lang="en">
<head>
<meta charset="UTF-8">
<title>Crestline Gas &amp; Plumbing – Business Card</title>
<link rel="stylesheet" href="https://fonts.googleapis.com/css2?family=Montserrat:wght@700&family=Lato:wght@400&display=swap">
<style>
  :root {
    --canvas-bg: #3b3b3b;
    --card-bg: #1f1f1f;
    --brand-blue: #2f6fc4;
    --brand-orange: #f0962a;
    --text-light: #d6d6d6;
  }
  * { margin: 0; padding: 0; box-sizing: border-box; }
  html, body {
    width: 1200px;
    height: 1200px;
    overflow: hidden;
    background: var(--canvas-bg);
  }
  .canvas {
    position: relative;
    width: 1200px;
    height: 1200px;
  }
  .card {
    position: absolute;
    background: var(--card-bg);
  }
  .card-front {
    left: 188px; top: 86px;
    width: 822px; height: 476px;
    display: flex;
    align-items: center;
    justify-content: center;
  }
  .card-back {
    left: 186px; top: 640px;
    width: 839px; height: 468px;
  }
  .brand-mark {
    display: flex;
    align-items: center;
    gap: 14px;
    font-family: "Montserrat", sans-serif;
    font-weight: 700;
    color: var(--brand-blue);
    text-transform: uppercase;
    letter-spacing: 1px;
  }
  .brand-dot {
    border-radius: 50%;
    background: var(--brand-orange);
    flex: none;
  }
  .card-front .brand-mark { font-size: 34px; }
  .card-front .brand-dot { width: 30px; height: 30px; }
  .card-back .brand-mark {
    position: absolute;
    right: 46px;
    top: 96px;
    font-size: 22px;
  }
  .card-back .brand-dot { width: 22px; height: 22px; }
  .contact {
    position: absolute;
    left: 46px;
    top: 248px;
    font-family: "Lato", sans-serif;
  }
  .person-name {
    font-family: "Montserrat", sans-serif;
    font-weight: 700;
    font-size: 27px;
    color: var(--brand-blue);
    letter-spacing: 0.5px;
    line-height: 1.1;
  }
  .person-role {
    font-size: 25px;
    color: var(--brand-orange);
    line-height: 1.2;
  }
  .abn {
    margin-top: 26px;
    font-size: 19px;
    color: var(--text-light);
  }
  .abn-label { color: var(--brand-blue); }
  .contact-line {
    display: flex;
    align-items: center;
    gap: 8px;
    font-size: 19px;
    color: var(--text-light);
    line-height: 27px;
  }
  .contact-line.phone { margin-top: 18px; }
  .contact-line svg { width: 14px; height: 14px; flex: none; }
</style>
</head>
<body>
<main class="canvas">
  <section class="card card-front">
    <div class="brand-mark">
      <span class="brand-dot"></span>
      <span class="brand-name">Crestline Gas &amp; Plumbing</span>
    </div>
  </section>

  <section class="card card-back">
    <div class="brand-mark">
      <span class="brand-dot"></span>
      <span class="brand-name">Crestline Gas &amp; Plumbing</span>
    </div>

    <div class="contact">
      <h1 class="person-name">DALE WHITCOMBE</h1>
      <p class="person-role">Owner</p>
      <p class="abn"><span class="abn-label">ABN</span> - 68204915336</p>
      <p class="contact-line phone">
        <svg viewBox="0 0 24 24" aria-hidden="true"><path fill="#f0962a" d="M6.6 10.8a15.1 15.1 0 0 0 6.6 6.6l2.2-2.2c.3-.3.7-.4 1-.2 1.1.4 2.3.6 3.6.6.6 0 1 .4 1 1V20c0 .6-.4 1-1 1A17 17 0 0 1 3 4c0-.6.4-1 1-1h3.5c.6 0 1 .4 1 1 0 1.3.2 2.5.6 3.6.1.3 0 .7-.2 1z"/></svg>
        0455163027
      </p>
      <p class="contact-line email">
        <svg viewBox="0 0 24 24" aria-hidden="true"><rect x="2" y="5" width="20" height="14" rx="1" fill="#f0962a"/><path d="M3 6l9 7 9-7" fill="none" stroke="#1f1f1f" stroke-width="1.8"/></svg>
        admin@crestlinegasandplumbing.example.com.au
      </p>
    </div>
  </section>
</main>
</body>
</html>
```